Business Card Design Project

Velvet Harbor is a Boutique Clothing. On the business cards I would like to have this included
Website: www.velvetharbor-example.com
Email: shop@velvetharbor-example.com
Owner: Mira Sol & Tor Dell

Industry/Entity Type

Business

Contact Information for Business Card

I wanted something simple and elegant. I have attach business logo.

```html
<!DOCTYPE html>
<html lang="en">
<head>
<meta charset="UTF-8">
<title>Velvet Harbor — Business Card</title>
<link rel="stylesheet" href="https://fonts.googleapis.com/css2?family=Roboto:ital,wght@0,400;0,700;1,400&display=swap">
<style>
  :root {
    --backdrop: #ecebe8;
    --card: #ffffff;
    --ink: #1e1e1e;
    --ink-soft: #3a3a3a;
    --shadow: rgba(0, 0, 0, 0.14);
  }
  * { box-sizing: border-box; margin: 0; padding: 0; }
  html, body {
    width: 1200px;
    height: 800px;
    overflow: hidden;
    background: var(--backdrop);
    font-family: "Roboto", Arial, sans-serif;
    color: var(--ink);
  }
  .canvas {
    position: relative;
    width: 1200px;
    height: 800px;
    display: flex;
    align-items: center;
    justify-content: center;
    gap: 60px;
  }
  .card {
    position: relative;
    width: 520px;
    height: 297px;
    background: var(--card);
    box-shadow: 0 10px 28px var(--shadow);
  }
  .brand {
    display: flex;
    align-items: center;
    gap: 12px;
    font-family: "Roboto", Arial, sans-serif;
    font-weight: 400;
    font-size: 22px;
    letter-spacing: 0.28em;
    text-transform: uppercase;
    color: var(--ink);
    white-space: nowrap;
  }
  .brand-dot {
    width: 8px;
    height: 8px;
    border-radius: 50%;
    background: var(--ink);
    flex: none;
  }
  .card--back {
    display: flex;
    align-items: center;
    justify-content: center;
  }
  .card--front .owners {
    position: absolute;
    left: 44px;
    top: 58px;
  }
  .owners-names {
    font-weight: 700;
    font-size: 16px;
    color: var(--ink);
  }
  .owners-role {
    font-style: italic;
    font-size: 14px;
    color: var(--ink-soft);
    margin-top: 2px;
  }
  .divider {
    position: absolute;
    left: 40px;
    top: 128px;
    width: 196px;
    height: 1.5px;
    background: var(--ink);
  }
  .contact {
    position: absolute;
    left: 36px;
    top: 172px;
    list-style: none;
    font-size: 14px;
    line-height: 1.45;
    color: var(--ink);
  }
  .card--front .brand {
    position: absolute;
    right: 34px;
    top: 50%;
    transform: translateY(-50%);
    flex-direction: column;
    gap: 8px;
    font-size: 18px;
    text-align: center;
  }
</style>
</head>
<body>
  <main class="canvas">
    <section class="card card--back" aria-label="Card back">
      <div class="brand">
        <span class="brand-dot"></span>
        <span class="brand-name">Velvet Harbor</span>
      </div>
    </section>

    <section class="card card--front" aria-label="Card front">
      <div class="owners">
        <p class="owners-names">Mira Sol &amp; Tor Dell</p>
        <p class="owners-role">owner</p>
      </div>
      <div class="divider"></div>
      <ul class="contact">
        <li>555 014 2290</li>
        <li>www.velvetharbor-example.com</li>
        <li>shop@velvetharbor-example.com</li>
      </ul>
      <div class="brand">
        <span class="brand-dot"></span>
        <span class="brand-name">Velvet<br>Harbor</span>
      </div>
    </section>
  </main>
</body>
</html>
```